Entrepreneur Podcast Cover Graphic Design

My wife and I just launched our podcast but we don't like the current cover. We want a new cover designed so it stands out and reflects the professionalism of our podcast. Attached is our current podcast cover design. We'd like to have it read "Rob & Kalinda Interview Entrepreneurs on HARD TURNS" - We'd also like to feature somehow that we have daily tips included.

Target Market(s)

entrepreneurs,business owners,start ups

Industry/Entity Type

Entrepreneur

Font styles to use
Sans Serif

Colors
0355a3
f37122
9bcb3c
fbed22
ec1f27

Requirements
Must have
• Our names listed: Rob & Kalinda
Nice to have
• dark, bold colored background with an outline around the edge
Should not have
• no cartoons, no profanity

```html
<!DOCTYPE html>
<html lang="en">
<head>
<meta charset="utf-8">
<title>Rob &amp; Kalinda Interview Entrepreneurs on HARD TURNS</title>
<link rel="stylesheet" href="https://fonts.googleapis.com/css2?family=Roboto:wght@300;700;900&display=swap">
<style>
  :root {
    --cream: #fec96a;
    --red: #ec1f27;
    --deep-red: #b3161c;
    --orange: #f37122;
    --tip-red: #d4141c;
  }
  html, body {
    margin: 0;
    padding: 0;
    width: 1200px;
    height: 1200px;
    overflow: hidden;
    background: var(--cream);
  }
  .cover {
    display: block;
    width: 1200px;
    height: 1200px;
  }
  .cover-bg { fill: var(--cream); }
  .bubble-main { fill: var(--red); }
  .bubble-echo { fill: var(--orange); }
  .hosts, .tagline, .headline {
    font-family: "Roboto", Arial, sans-serif;
    fill: var(--cream);
    text-anchor: middle;
    filter: drop-shadow(4px 4px 0 var(--deep-red));
  }
  .hosts { font-weight: 700; font-size: 154px; letter-spacing: -1px; }
  .tagline { font-weight: 300; font-size: 86px; }
  .headline { font-weight: 700; }
  .headline-top { font-size: 306px; letter-spacing: -4px; }
  .headline-bottom { font-size: 250px; letter-spacing: -3px; }
  .daily-tips {
    font-family: "Roboto", Arial, sans-serif;
    font-weight: 300;
    font-size: 86px;
    fill: var(--tip-red);
  }
  .tick {
    fill: none;
    stroke: var(--tip-red);
    stroke-width: 10;
    stroke-linecap: round;
    stroke-linejoin: round;
  }
</style>
</head>
<body>
<svg class="cover" viewBox="0 0 1200 1200" xmlns="http://www.w3.org/2000/svg">
  <rect class="cover-bg" width="1200" height="1200"/>

  <g class="bubbles" transform="scale(0.8)">
    <g class="bubble-echo">
      <ellipse cx="1150" cy="1115" rx="310" ry="140"/>
      <path d="M1170 1230 Q1150 1280 1125 1315 Q1115 1330 1135 1325 Q1220 1300 1265 1240 Z"/>
    </g>
    <g class="bubble-main">
      <ellipse cx="750" cy="575" rx="1032" ry="575"/>
      <path d="M330 1080 Q470 1315 800 1350 Q850 1345 825 1315 Q745 1235 695 1145 Z"/>
    </g>
  </g>

  <text class="hosts" x="603" y="232">Rob &amp; Kalinda</text>
  <text class="tagline" x="600" y="332">Interview Entrepreneurs on</text>
  <text class="headline headline-top" x="600" y="608">HARD</text>
  <text class="headline headline-bottom" x="600" y="796">TURNS</text>

  <polyline class="tick" points="216,1112 236,1142 284,1090"/>
  <text class="daily-tips" x="316" y="1156">Includes daily tips</text>
</svg>
</body>
</html>
```